Automotive parts Package (box) design

We are developing a new packaging concept for our automotive service and suspension parts line. I will share 2–3 sample designs—some from other brands and some AI‑generated—and we need a designer to create a unified, original design direction based on these references.

We already have an established brand name, KEM, along with a logo. The logo may be updated or redesigned, but the brand name KEM must remain.

- The project includes creating the full packaging design for our product boxes, developing or refining the logo if needed.

-Then, after choosing the design, we will apply the same design to 8 boxes with small customisation for each box to match the product.

- The box die-lines will be provided by us.

Attached are a few sample designs. We need you to develop three or more new designs in a similar style. If you have additional creative concepts beyond these references, you are welcome to include them. The only fixed requirement is that the brand name KEM must remain unchanged in all proposed designs.

Box files such as PNG, PDF (ready-to-print file) and Ai (Editable/ Source file) and fonts with 3D mockup images at the end of the project must be given to us.

Target Market(s)

Car spare parts shops

Industry/Entity Type

Auto Parts

Requirements
Must have
• Our brand name KEM
Nice to have
• Package similar to big auto parts suppliers such as PLW, VARNE

```html
<!DOCTYPE html>
<html lang="en">
<head>
<meta charset="utf-8">
<title>KEM Automotive Components – Box Panel</title>
<link href="https://fonts.googleapis.com/css2?family=Anton&family=Montserrat:wght@800&display=swap" rel="stylesheet">
<style>
  :root {
    --ink: #000000;
    --paper: #ffffff;
    --brand-red: #c91515;
    --stage: #fbfbfb;
  }
  html, body {
    margin: 0;
    padding: 0;
    width: 1200px;
    height: 2464px;
    overflow: hidden;
    background: var(--stage);
  }
  .box-panel {
    position: absolute;
    left: 14px;
    top: 140px;
    width: 1157px;
    height: 356px;
    box-shadow: 0 30px 50px rgba(0,0,0,0.12);
  }
  .box-panel svg {
    display: block;
  }
  .brand-name {
    font-family: "Anton", sans-serif;
    font-size: 150px;
    fill: var(--paper);
    letter-spacing: 2px;
  }
  .brand-tagline {
    font-family: "Anton", sans-serif;
    font-size: 29px;
    fill: var(--paper);
    letter-spacing: 1px;
  }
  .product-line {
    font-family: "Montserrat", sans-serif;
    font-weight: 800;
    font-size: 15px;
    fill: var(--paper);
    letter-spacing: 0.5px;
  }
  .cert-text {
    font-family: "Montserrat", sans-serif;
    font-weight: 800;
    font-size: 15px;
    fill: var(--ink);
  }
</style>
</head>
<body>
  <div class="box-panel">
    <svg width="1157" height="356" viewBox="0 0 1157 356" xmlns="http://www.w3.org/2000/svg">
      <defs>
        <linearGradient id="shaft-tone" x1="0" y1="0" x2="1" y2="0">
          <stop offset="0" stop-color="#f2f2f2"/>
          <stop offset="0.55" stop-color="#e6e6e6"/>
          <stop offset="0.6" stop-color="#b81212"/>
          <stop offset="1" stop-color="#b81212"/>
        </linearGradient>
      </defs>

      <!-- base -->
      <rect class="panel-base" x="0" y="0" width="1157" height="356" fill="var(--ink)"/>

      <!-- white sweep -->
      <path class="white-sweep" d="M351 0 L691 0 C735 60 758 110 754 180 C750 250 715 300 668 356 L364 356 L351 300 Z" fill="var(--paper)"/>

      <!-- logo block -->
      <polygon class="logo-block" points="0,12 351,82 351,278 96,356 0,356" fill="var(--ink)"/>

      <!-- red corner -->
      <polygon class="red-corner" points="96,356 301,292 364,356" fill="var(--brand-red)"/>

      <!-- red band -->
      <path class="red-band" d="M752 104 L1157 104 L1157 248 L747 248 C752 200 754 150 752 104 Z" fill="var(--brand-red)"/>

      <!-- certification tag -->
      <polygon class="cert-tag" points="1034,60 1157,15 1157,170 1034,132" fill="var(--paper)"/>
      <text class="cert-text" text-anchor="middle">
        <tspan x="1106" y="79">ISO 9001</tspan>
        <tspan x="1106" y="99">CERTIFIED</tspan>
        <tspan x="1106" y="119">MADE IN</tspan>
        <tspan x="1106" y="139">GERMANY</tspan>
      </text>

      <!-- product drawing area -->
      <rect class="product-drawing" role="img" aria-label="Line drawing of a CV drive shaft with boots at both ends"
            x="381" y="122" width="660" height="135" fill="url(#shaft-tone)"/>

      <!-- brand -->
      <text class="brand-name" x="10" y="228">KEM</text>
      <text class="brand-tagline" x="10" y="265">AUTOMOTIVE COMPONENTS</text>

      <!-- product line -->
      <text class="product-line" x="838" y="320">STEERING &amp; SUSPENSION PARTS</text>
    </svg>
  </div>
</body>
</html>
```